Hollowbrook Print and Ink Business

Hi, I need template designs for stationary as listed below using my Logo as per attached file;
1) Business Card (double sided)
2) Letterhead
3) With Compliments Slip
4) Return Address Label (Stickers)

```html
<!DOCTYPE html>
<html lang="en">
<head>
<meta charset="utf-8">
<title>Hollowbrook Print and Ink — Stationery</title>
<link rel="stylesheet" href="https://fonts.googleapis.com/css2?family=Poppins:wght@400;600&display=swap">
<style>
  :root {
    --backdrop: #ecebe8;
    --paper: #ffffff;
    --magenta: #d455b8;
    --mint: #6de28e;
    --ink: #5a5a5a;
    --ink-soft: #8a8a8a;
    --rule: #6f6f6f;
    --shadow: 0 6px 18px rgba(0,0,0,0.14);
  }
  * { box-sizing: border-box; margin: 0; padding: 0; }
  html, body { width: 1200px; height: 800px; overflow: hidden; }
  body {
    position: relative;
    background: var(--backdrop);
    font-family: "Poppins", sans-serif;
    color: var(--ink);
  }

  .brand-name {
    display: flex;
    align-items: center;
    gap: 10px;
    font-weight: 600;
    line-height: 1.15;
    white-space: nowrap;
  }
  .brand-name .brand-lines { display: flex; flex-direction: column; }
  .brand-name .brand-dot {
    flex: none;
    width: 12px; height: 12px;
    border-radius: 50%;
    background: currentColor;
  }

  /* Letterhead */
  .letterhead {
    position: absolute;
    left: 40px; top: 40px;
    width: 360px; height: 510px;
    background: var(--paper);
    box-shadow: var(--shadow);
    padding: 40px 36px;
  }
  .letterhead .brand-name {
    justify-content: center;
    font-size: 15px;
    margin-bottom: 40px;
  }
  .letterhead .letter-body {
    font-size: 10px;
    line-height: 1.9;
    color: var(--ink-soft);
  }
  .letterhead .letter-body p + p { margin-top: 14px; }

  /* Business card front */
  .square-card {
    position: absolute;
    left: 450px; top: 60px;
    width: 260px; height: 260px;
    background: var(--magenta);
    box-shadow: var(--shadow);
    display: flex;
    align-items: center;
    justify-content: center;
  }
  .square-card .brand-name {
    color: var(--paper);
    font-size: 24px;
    gap: 14px;
  }
  .square-card .brand-dot { width: 56px; height: 56px; }

  /* Business card back */
  .business-card {
    position: absolute;
    left: 760px; top: 110px;
    width: 380px; height: 210px;
    background: var(--paper);
    box-shadow: var(--shadow);
    padding: 28px 30px;
  }
  .business-card .brand-name { font-size: 16px; }
  .business-card .brand-dot { width: 18px; height: 18px; }
  .business-card .write-lines {
    position: absolute;
    right: 30px; bottom: 40px;
    width: 170px;
  }

  /* Compliments slip */
  .comp-slip {
    position: absolute;
    left: 450px; top: 380px;
    width: 690px; height: 340px;
    background: var(--mint);
    box-shadow: var(--shadow);
    padding: 30px 34px;
  }
  .comp-slip .slip-header { font-size: 16px; }
  .comp-slip .slip-feature {
    position: absolute;
    left: 80px; top: 120px;
    font-size: 34px;
    gap: 18px;
  }
  .comp-slip .slip-feature .brand-dot { width: 90px; height: 90px; }
  .comp-slip .write-lines {
    position: absolute;
    right: 50px; top: 190px;
    width: 240px;
  }
  .comp-slip .slip-footer {
    position: absolute;
    right: 50px; bottom: 30px;
    font-size: 9px;
    letter-spacing: 0.4em;
  }

  .write-lines .line {
    height: 1px;
    background: var(--rule);
    margin-top: 20px;
  }
</style>
</head>
<body>

  <section class="letterhead" aria-label="Letterhead">
    <div class="brand-name"><span class="brand-dot"></span>Hollowbrook Print and Ink</div>
    <div class="letter-body">
      <p>Dear client, thank you for choosing our studio. We look forward to working with you on every print project ahead.</p>
      <p>Our team prepares each proof with care and will send it for your approval before anything goes to press.</p>
      <p>Kind regards</p>
      <p>The Hollowbrook team</p>
    </div>
  </section>

  <section class="square-card" aria-label="Business card front">
    <div class="brand-name">
      <span class="brand-dot"></span>
      <span class="brand-lines"><span>Hollowbrook</span><span>Print and Ink</span></span>
    </div>
  </section>

  <section class="business-card" aria-label="Business card back">
    <div class="brand-name">
      <span class="brand-dot"></span>
      <span class="brand-lines"><span>Hollowbrook</span><span>Print and Ink</span></span>
    </div>
    <div class="write-lines">
      <div class="line"></div>
      <div class="line"></div>
      <div class="line"></div>
    </div>
  </section>

  <section class="comp-slip" aria-label="With compliments slip">
    <div class="brand-name slip-header">
      <span class="brand-lines"><span>Hollowbrook</span><span>Print and Ink</span></span>
    </div>
    <div class="brand-name slip-feature">
      <span class="brand-dot"></span>
      <span class="brand-lines"><span>Hollowbrook</span><span>Print and Ink</span></span>
    </div>
    <div class="write-lines">
      <div class="line"></div>
      <div class="line"></div>
      <div class="line"></div>
    </div>
    <div class="slip-footer">PRINT AND INK</div>
  </section>

</body>
</html>
```